Business Card Design for Lawn Management

Lawn Management

Industry/Entity Type

Business

Contact Information for Business Card

Calloway Lawn Management
Joel Calloway
Calloway_Lawn@brindlemail.com
404-555-0172

```html
<!DOCTYPE html>
<html lang="en">
<head>
<meta charset="utf-8">
<title>Calloway Lawn Management – Business Card</title>
<link href="https://fonts.googleapis.com/css2?family=Roboto:wght@400;500;700;900&display=swap" rel="stylesheet">
<style>
  :root {
    --page-bg: #ecebe7;
    --card-white: #f7f8f7;
    --grass-light: #a6dc4a;
    --grass-mid: #6cbf2a;
    --grass-deep: #3f8f1c;
    --accent-green: #5cc93a;
    --ink-dark: #1f2224;
    --ink-soft: #3a3d40;
    --white: #ffffff;
  }
  * { margin: 0; padding: 0; box-sizing: border-box; }
  html, body {
    width: 1200px; height: 1000px; overflow: hidden;
    background: var(--page-bg);
    font-family: "Roboto", Arial, sans-serif;
  }
  .card {
    position: absolute; left: 220px;
    width: 760px; height: 434px;
    border-radius: 4px; overflow: hidden;
    box-shadow: 0 10px 28px rgba(0,0,0,0.18);
  }
  .card--back { top: 44px; }
  .card--front { top: 522px; background: var(--card-white); }

  .grass-field { position: absolute; inset: 0; width: 100%; height: 100%; }

  .brand {
    position: absolute; color: var(--white);
    font-weight: 700; text-align: center;
    display: flex; flex-direction: column; align-items: center;
  }
  .brand__dot {
    width: 74px; height: 74px; border-radius: 50%;
    background: var(--white); margin-bottom: 18px;
  }
  .brand__name { font-size: 44px; line-height: 1; letter-spacing: 1px; text-transform: uppercase; }
  .brand__sub { font-size: 24px; line-height: 1.3; font-weight: 400; }

  .card--back .brand { left: 0; right: 0; top: 110px; }
  .card--front .brand { left: 30px; width: 300px; top: 60px; }
  .card--front .brand__dot { width: 62px; height: 62px; margin-bottom: 16px; }
  .card--front .brand__name { font-size: 38px; }
  .card--front .brand__sub { font-size: 20px; }

  .holder {
    position: absolute; right: 56px; top: 150px; text-align: right;
    white-space: nowrap;
  }
  .holder__name {
    font-size: 32px; font-weight: 900; letter-spacing: 1.5px;
    color: var(--ink-dark); text-transform: uppercase;
  }
  .holder__first { color: var(--accent-green); }
  .holder__role {
    margin-top: 6px; font-size: 13px; font-weight: 500;
    letter-spacing: 1.5px; color: var(--ink-soft); text-transform: uppercase;
  }
  .holder__role .slash { color: var(--accent-green); }

  .contact {
    position: absolute; left: 292px; right: 40px; top: 342px;
    display: flex; justify-content: space-between; align-items: baseline;
    gap: 20px; white-space: nowrap;
    font-size: 15px; color: var(--ink-soft);
  }
  .contact__label { color: var(--accent-green); font-weight: 700; letter-spacing: 1px; }
</style>
</head>
<body>

  <section class="card card--back">
    <svg class="grass-field" viewBox="0 0 760 434" role="img" aria-label="Close-up photo of fresh green lawn grass">
      <defs>
        <linearGradient id="grassBack" x1="0" y1="0" x2="1" y2="1">
          <stop offset="0" stop-color="#a6dc4a"/>
          <stop offset="0.55" stop-color="#6cbf2a"/>
          <stop offset="1" stop-color="#3f8f1c"/>
        </linearGradient>
      </defs>
      <rect width="760" height="434" fill="url(#grassBack)"/>
    </svg>
    <div class="brand">
      <span class="brand__dot"></span>
      <span class="brand__name">Calloway</span>
      <span class="brand__sub">Lawn Management</span>
    </div>
  </section>

  <section class="card card--front">
    <svg class="grass-field" viewBox="0 0 760 434">
      <defs>
        <linearGradient id="grassFront" x1="0" y1="0" x2="0.6" y2="1">
          <stop offset="0" stop-color="#a6dc4a"/>
          <stop offset="0.6" stop-color="#6cbf2a"/>
          <stop offset="1" stop-color="#3f8f1c"/>
        </linearGradient>
      </defs>
      <polygon points="0,0 440,0 240,434 0,434" fill="url(#grassFront)"
               role="img" aria-label="Close-up photo of fresh green lawn grass"/>
      <g class="divider-lines" stroke="#5cc93a" stroke-width="1.4">
        <line x1="452" y1="0" x2="332" y2="260"/>
        <line x1="462" y1="0" x2="350" y2="243"/>
        <line x1="472" y1="0" x2="368" y2="226"/>
      </g>
    </svg>

    <div class="brand">
      <span class="brand__dot"></span>
      <span class="brand__name">Calloway</span>
      <span class="brand__sub">Lawn Management</span>
    </div>

    <div class="holder">
      <h1 class="holder__name"><span class="holder__first">Joel</span> Calloway</h1>
      <p class="holder__role">Professional<span class="slash">/</span>Landscape<span class="slash">/</span>Lawn Care</p>
    </div>

    <div class="contact">
      <p class="contact__phone"><span class="contact__label">OFFICE</span> : 404-555-0172</p>
      <p class="contact__email">Calloway_Lawn@brindlemail.com</p>
    </div>
  </section>

</body>
</html>
```